Business Card Design

We need a design for business cards for our company. We have a logo. We train new medics for work in the field, every day. The information that will need to add would be, name, title, phone number, email, address. On the back of the business card would be "Learn It Here, Use It There"

Target Market(s)

People that want to become EMT's

Colors

Designer to choose colors to be used in the design.

Requirements
Must have
• company logo

```html
<!DOCTYPE html>
<html lang="en">
<head>
<meta charset="utf-8">
<title>Medic Path Academy – Business Card</title>
<link rel="stylesheet" href="https://fonts.googleapis.com/css2?family=Lexend:wght@300;400;500&display=swap">
<style>
  :root {
    --page: #ffffff;
    --frame: #e31e26;
    --card: #222d36;
    --ink: #ffffff;
    --brand: #e8203c;
  }
  * { box-sizing: border-box; margin: 0; padding: 0; }
  html, body { width: 977px; height: 1200px; overflow: hidden; background: var(--page); }
  body { font-family: "Lexend", sans-serif; color: var(--ink); position: relative; }

  .sheet-frame {
    position: absolute; inset: 0;
    border: 10px solid var(--frame);
  }
  .card {
    position: absolute; left: 109px; width: 769px; height: 491px;
    background: var(--card);
  }
  .card--front { top: 79px; }
  .card--back { top: 632px; display: flex; align-items: center; justify-content: center; }

  .brand {
    position: absolute; top: 90px; left: 0; right: 0;
    display: flex; align-items: center; justify-content: center; gap: 12px;
  }
  .brand__dot { width: 16px; height: 16px; border-radius: 50%; background: var(--brand); }
  .brand__name {
    font-size: 30px; font-weight: 500; color: var(--brand); letter-spacing: 1px;
    text-transform: uppercase;
  }

  .person__name {
    position: absolute; right: 68px; top: 237px;
    font-size: 23px; font-weight: 400; white-space: nowrap;
  }
  .person__rule {
    position: absolute; left: 57px; top: 278px; width: 537px; height: 2px; background: var(--ink);
  }
  .person__title {
    position: absolute; right: 73px; top: 265px;
    font-size: 17px; font-weight: 300; white-space: nowrap;
  }

  .contact { position: absolute; left: 0; top: 0; list-style: none; }
  .contact__item {
    position: absolute; left: 56px; display: flex; align-items: center;
    font-size: 17px; font-weight: 300; white-space: nowrap; height: 20px;
  }
  .contact__item:nth-child(1) { top: 345px; }
  .contact__item:nth-child(2) { top: 374px; }
  .contact__item:nth-child(3) { top: 403px; }
  .contact__icon { width: 16px; height: 16px; margin-right: 20px; flex: none; }

  .divider {
    position: absolute; left: 401px; top: 332px; width: 2px; height: 107px; background: var(--ink);
  }
  .about {
    position: absolute; left: 451px; top: 380px;
    font-size: 17.5px; font-weight: 300; line-height: 29px; white-space: nowrap;
  }

  .motto { font-size: 40px; font-weight: 400; white-space: nowrap; }
</style>
</head>
<body>
  <div class="sheet-frame"></div>

  <section class="card card--front">
    <div class="brand">
      <span class="brand__dot"></span>
      <span class="brand__name">Medic Path Academy</span>
    </div>

    <p class="person__name">Your Name John Doe</p>
    <div class="person__rule"></div>
    <p class="person__title">Your title</p>

    <ul class="contact">
      <li class="contact__item">
        <svg class="contact__icon" viewBox="0 0 16 16" aria-hidden="true">
          <rect x="4" y="1" width="8" height="14" rx="1.5" fill="none" stroke="#fff" stroke-width="1.5"/>
          <rect x="5.5" y="3" width="5" height="6" fill="#fff"/>
          <circle cx="8" cy="12.5" r="1" fill="#fff"/>
        </svg>
        555.210.4836
      </li>
      <li class="contact__item">
        <svg class="contact__icon" viewBox="0 0 16 16" aria-hidden="true">
          <rect x="1" y="3.5" width="14" height="9.5" fill="#fff"/>
          <path d="M1 3.5 L8 9 L15 3.5" fill="none" stroke="#222d36" stroke-width="1.4"/>
        </svg>
        emailaddress@medicpath.com
      </li>
      <li class="contact__item">
        <svg class="contact__icon" viewBox="0 0 16 16" aria-hidden="true">
          <g fill="none" stroke="#fff" stroke-width="2" stroke-linecap="round">
            <path d="M7 9.5 L5 11.5 a2.4 2.4 0 0 1 -3.4 -3.4 L4 5.7"/>
            <path d="M9 6.5 L11 4.5 a2.4 2.4 0 0 1 3.4 3.4 L12 10.3"/>
            <path d="M6 10 L10 6"/>
          </g>
        </svg>
        www.medicpathacademy.com
      </li>
    </ul>

    <div class="divider"></div>
    <p class="about">We train new medics for<br>work in the field, every day.</p>
  </section>

  <section class="card card--back">
    <p class="motto">Learn It Here, Use It There</p>
  </section>
</body>
</html>
```